Presentation Folder for A New Home Construction Company

We need a Presentation Folder for a new home construction company based in Perth, Australia. It's called Tarvo Homes and specialises in building quality homes that are affordable and people want to live in. The target market is first-home buyers.

We've rebranded the website (www.tarvohomes.com.au) and are looking to update our presentation folder to match it. We want red, white, grey and black as the colour palette, and some designs with transparent photos included but overall a minimalistic approach that aligns with our new website and vehicles.

I've attached an image of our updated car wrap, can you please follow this as a guide?

I've also attached our logo, style guide and past presentation folder for reference.

Please also include:

"Plan Well, Move In, Stay Put" - refer to the previous presentation folder.

Target Market(s)

First Home Buyers

Industry/Entity Type

New Home Construction

Font styles to use
Sans Serif
Other font styles liked:
• Monserrat

Colors
EB3D1F
EC4F4E
F09395
F8D3D4
FCEDEE

Requirements
Must have
• Monserrat or Open Sans Font and Include the colours from the attached brand guide, the contact details and address,
Nice to have
• some with a photo feature - but not the main component, very minimal.
Should not have
• Too many elements, (refer to previous folder attachment) animations or graphics.

```html
<!DOCTYPE html>
<html lang="en">
<head>
<meta charset="utf-8">
<title>Tarvo Homes – Presentation Folder</title>
<link rel="stylesheet" href="https://fonts.googleapis.com/css2?family=Poppins:wght@400;500;600;700;800&display=swap">
<style>
  :root {
    --brand-red: #d90000;
    --panel-white: #ffffff;
    --ink-black: #111111;
    --page-bg: #ffffff;
    --photo-dark: #4a5563;
    --photo-light: #c9ccd1;
  }
  * { margin: 0; padding: 0; box-sizing: border-box; }
  html, body { width: 734px; height: 1200px; overflow: hidden; background: var(--page-bg); }
  body { font-family: "Poppins", sans-serif; color: var(--panel-white); }
  .canvas { position: relative; width: 734px; height: 1200px; }
  .folder { position: absolute; left: 25px; top: 350px; width: 683px; height: 502px; }
  .folder-shape { position: absolute; inset: 0; filter: drop-shadow(0 3px 6px rgba(0,0,0,.18)); }

  .headline { position: absolute; left: 415px; top: 24px; font-weight: 700; font-size: 39px; line-height: 36px; letter-spacing: -0.5px; white-space: nowrap; }
  .headline-accent { display: inline-block; background: var(--ink-black); color: var(--brand-red); padding: 0 5px; line-height: 30px; border-radius: 2px; }

  .spine-tagline { position: absolute; left: 194px; top: 114px; font-weight: 600; font-size: 8px; white-space: nowrap; }
  .brand-name { font-weight: 700; color: var(--panel-white); white-space: nowrap; }
  .brand-name--small { position: absolute; left: 208px; top: 128px; font-size: 13px; line-height: 16px; }
  .brand-name--large { position: absolute; left: 415px; top: 302px; font-size: 22px; line-height: 25px; }

  .photo-feature { position: absolute; left: 112px; top: 241px; width: 90px; height: 158px;
    background: linear-gradient(160deg, var(--photo-light), var(--photo-dark)); }

  .intro { position: absolute; left: 204px; top: 238px; width: 170px; font-size: 8.6px; line-height: 10.5px; }
  .intro-highlight { display: block; font-weight: 700; font-size: 13px; line-height: 20px; margin-top: 1px; }

  .contact-list { position: absolute; left: 222px; top: 302px; list-style: none; font-weight: 600; font-size: 6.2px; line-height: 7.4px; white-space: nowrap; }
  .contact-list li { display: flex; gap: 4px; margin-bottom: 3px; }
  .contact-list svg { flex: none; width: 6px; height: 6px; margin-top: 1px; }

  .name-badge { position: absolute; left: 211px; top: 361px; width: 104px; height: 15px; background: var(--ink-black); border-radius: 2px;
    display: flex; align-items: center; gap: 4px; padding-left: 10px; white-space: nowrap; }
  .name-badge-name { font-weight: 700; font-size: 9px; line-height: 15px; letter-spacing: -0.2px; }
  .name-badge-role { font-size: 4px; line-height: 4.2px; text-transform: uppercase; }

  .website { position: absolute; left: 279px; top: 382px; font-weight: 700; font-size: 6.8px; letter-spacing: .6px; white-space: nowrap; }
</style>
</head>
<body>
<main class="canvas">
  <section class="folder" aria-label="Tarvo Homes presentation folder, flat layout">
    <svg class="folder-shape" viewBox="0 0 683 502" width="683" height="502" aria-hidden="true">
      <rect class="folder-panel" x="0" y="0" width="683" height="399" fill="var(--brand-red)"/>
      <path class="pocket-flap" d="M112,399 L112,406 L141,440 L128,450 L128,456 L149,476 L165,467 L196,501 L346,501 Q384,501 384,463 L384,399 Z" fill="var(--brand-red)"/>
      <path class="cover-panel" d="M683,165 L570,165 Q505,165 505,240 L505,399 L683,399 Z" fill="var(--panel-white)"/>
    </svg>

    <h1 class="headline">PLAN WELL<br>MOVE IN<br>STAY <span class="headline-accent">PUT</span></h1>

    <p class="spine-tagline">PLAN WELL... MOVE IN...</p>
    <p class="brand-name brand-name--small">Tarvo Homes</p>

    <div class="photo-feature" role="img" aria-label="Cut-out photo of the managing director leaning on a tablet"></div>

    <p class="intro">Offering first home buyers the same outstanding service &amp; innovation that has been Dean Harlow’s hallmark for
      <span class="intro-highlight">Over 15 years..</span></p>

    <ul class="contact-list">
      <li><svg viewBox="0 0 10 10"><path d="M5 0a3.5 3.5 0 0 0-3.5 3.5C1.5 6 5 10 5 10s3.5-4 3.5-6.5A3.5 3.5 0 0 0 5 0zm0 5a1.5 1.5 0 1 1 0-3 1.5 1.5 0 0 1 0 3z" fill="var(--ink-black)"/></svg>
        <span>41 Kestrel Road, Balcatta,<br>Western Australia 6021<br>PO Box 2280, Balcatta WA</span></li>
      <li><svg viewBox="0 0 10 10"><path d="M2 0l2 2.5-1 1.5a6 6 0 0 0 3 3l1.5-1L10 8l-1.5 2C4 10 0 6 0 1.5z" fill="var(--ink-black)"/></svg><span>08 9470 2215</span></li>
      <li><svg viewBox="0 0 10 10"><rect x="2.5" y="0" width="5" height="3" fill="var(--ink-black)"/><rect x="0" y="3.5" width="10" height="4" rx="1" fill="var(--ink-black)"/><rect x="2.5" y="7" width="5" height="3" fill="var(--ink-black)"/></svg><span>08 9470 2216</span></li>
      <li><svg viewBox="0 0 10 10"><rect x="0" y="2" width="10" height="6.5" fill="var(--ink-black)"/><path d="M0 2l5 3.5L10 2" stroke="var(--brand-red)" fill="none" stroke-width="1"/></svg><span>hello@tarvohomes.com.au</span></li>
    </ul>

    <div class="name-badge">
      <span class="name-badge-name">DEAN HARLOW</span>
      <span class="name-badge-role">Managing<br>Director</span>
    </div>

    <p class="website">www.TARVOHOMES.com.au</p>

    <p class="brand-name brand-name--large">Tarvo<br>Homes</p>
  </section>
</main>
</body>
</html>
```